Norvane Builders Business Card

Modern and Professional Business Card for a Med size construction/development company.

See the samples below for the design I like … but I need ideas for incorporating the red company logo while still keeping the clean look of the card samples that are attached.

Logo and tag line on the back … info on the front.

Tagline: Solid Work from the Footings Up

Target Market(s)

Med-Large General Contractors

Contact Information for Business Card

Norvane Builders Limited
42 Brenton Street
Elk Harbour, NL
B3K 7T2

t: 709-555-0147
f: 709-555-0192
w: www.norvanebuilders-example.com

Font styles to use
Sans Serif

Colors
fbee3e

Requirements
Must have
• I like the black and yellow designs of the attached samples …. but I'm not sure how to incorporate the red Norvane Builders logo into that design??
Nice to have
• Construction safety strips

```html
<!DOCTYPE html>
<html lang="en">
<head>
<meta charset="utf-8">
<title>Norvane Builders Business Card</title>
<link href="https://fonts.googleapis.com/css2?family=Montserrat:wght@400;500;600;700;800&family=Arimo:ital,wght@1,700&display=swap" rel="stylesheet">
<style>
  :root {
    --red: #f40206;
    --white: #ffffff;
    --ink: #4a4a4a;
    --stage: #8a8b98;
  }
  * { margin: 0; padding: 0; box-sizing: border-box; }
  html, body {
    width: 1200px; height: 1200px; overflow: hidden;
    background: var(--stage);
    font-family: "Montserrat", sans-serif;
  }
  .card {
    position: absolute;
    width: 696px; height: 415px;
    background: var(--white);
  }
  .card--front { left: 257px; top: 122px; }
  .card--back { left: 258px; top: 620px; }

  .front-panel { position: absolute; left: 0; top: 0; }
  .brand-name {
    position: absolute;
    color: var(--white);
    font-weight: 800;
    text-align: center;
    letter-spacing: 1px;
    line-height: 1.15;
  }
  .card--front .brand-name {
    left: 62px; top: 166px; width: 232px;
    font-size: 27px;
  }

  .person { position: absolute; left: 425px; top: 106px; color: var(--red); }
  .person__name { font-size: 19px; font-weight: 700; letter-spacing: 0.3px; }
  .person__title { font-size: 13.5px; font-weight: 500; margin-top: 1px; }

  .contact { position: absolute; left: 392px; top: 0; color: var(--ink); font-size: 14px; line-height: 17px; }
  .contact__row { position: absolute; left: 0; display: flex; white-space: nowrap; }
  .contact__icon { width: 18px; height: 18px; margin-right: 15px; flex: none; }
  .contact__address { top: 154px; }
  .contact__address .contact__icon { margin-top: 3px; }

  .back-panel {
    position: absolute; left: 22px; top: 20px;
    width: 653px; height: 377px;
    background: var(--red);
  }
  .card--back .brand-name {
    left: 0; top: 118px; width: 100%;
    font-size: 46px;
  }
  .tagline {
    position: absolute; left: 0; top: 312px; width: 100%;
    text-align: center;
    color: var(--white);
    font-family: "Arimo", sans-serif;
    font-style: italic; font-weight: 700;
    font-size: 20px; letter-spacing: 1.2px;
  }
</style>
</head>
<body>

<section class="card card--front">
  <svg class="front-panel" width="696" height="415" viewBox="0 0 696 415" aria-hidden="true">
    <polygon points="21,20 279,20 367,207 279,393 21,393" fill="var(--red)"/>
  </svg>
  <div class="brand-name">NORVANE<br>BUILDERS</div>

  <div class="person">
    <div class="person__name">YOUR NAME</div>
    <div class="person__title">Your Title/Designation</div>
  </div>

  <div class="contact">
    <svg style="position:absolute;left:8px;top:243px" width="2" height="60" aria-hidden="true">
      <line x1="1" y1="0" x2="1" y2="60" stroke="var(--red)" stroke-width="1.5"/>
    </svg>

    <div class="contact__row contact__address">
      <svg class="contact__icon" viewBox="0 0 18 18" aria-hidden="true">
        <circle cx="9" cy="9" r="8" fill="var(--red)"/>
        <circle cx="9" cy="8" r="2.3" fill="var(--white)"/>
      </svg>
      <div>Norvane Builders Limited<br>42 Brenton Street, Elk Harbour,<br>NL B3K 7T2</div>
    </div>

    <div class="contact__row" style="top:230px">
      <svg class="contact__icon" viewBox="0 0 18 18" aria-hidden="true">
        <circle cx="9" cy="9" r="8" fill="var(--red)"/>
        <path d="M6 5.5 L7.5 5 L8.5 7.3 L7.6 8.2 Q8.6 10 9.9 10.6 L10.8 9.7 L13 10.7 L12.6 12.2 Q8.5 12.6 6 8 Z" fill="var(--white)"/>
      </svg>
      <span>709-555-0147</span>
    </div>
    <div class="contact__row" style="top:254px">
      <svg class="contact__icon" viewBox="0 0 18 18" aria-hidden="true">
        <circle cx="9" cy="9" r="8" fill="var(--red)"/>
        <rect x="5.5" y="7" width="7" height="5" fill="var(--white)"/>
        <rect x="7" y="5" width="4" height="2" fill="var(--white)"/>
      </svg>
      <span>709-555-0192</span>
    </div>
    <div class="contact__row" style="top:273px">
      <svg class="contact__icon" viewBox="0 0 18 18" aria-hidden="true">
        <circle cx="9" cy="9" r="8" fill="var(--red)"/>
        <rect x="5.5" y="6.5" width="7" height="5" fill="var(--white)"/>
        <path d="M5.5 6.5 L9 9.3 L12.5 6.5" fill="none" stroke="var(--red)" stroke-width="0.8"/>
      </svg>
      <span>youremailaddress@.com</span>
    </div>
    <div class="contact__row" style="top:294px">
      <svg class="contact__icon" viewBox="0 0 18 18" aria-hidden="true">
        <circle cx="9" cy="9" r="8" fill="var(--red)"/>
        <circle cx="9" cy="9" r="3.6" fill="none" stroke="var(--white)" stroke-width="1"/>
        <line x1="5.4" y1="9" x2="12.6" y2="9" stroke="var(--white)" stroke-width="0.8"/>
        <line x1="9" y1="5.4" x2="9" y2="12.6" stroke="var(--white)" stroke-width="0.8"/>
      </svg>
      <span>www.norvanebuilders-example.com</span>
    </div>
  </div>
</section>

<section class="card card--back">
  <div class="back-panel">
    <div class="brand-name">NORVANE BUILDERS<br>LIMITED</div>
    <div class="tagline">Solid Work from the Footings Up</div>
  </div>
</section>

</body>
</html>
```